Hong Kong residential leasing and sales company needs a website design

Hong Kong has many competitive real estate agents. The majority of us have the same listings so, besides the team and experience, a website is what makes us stand out. A first impression. We need our website to be user friendly, informative and to have a wow factor. Most sites are generic so whilst we are close to accepting that maybe that's the only formula which works....we would like to see if we're missing something! Our clients are a mix of International users of all ages but probably ultimately 35+.. We have a logo (attached) which we would like to keep - designed by artmarketly. Flexible with colours except red.
examples of our competitors are:
http://www.brindlewoodestates.example
http://www.nuvo.example/home
http://www.premierdwellingsvx.example
http://www.orchid-lettings.example
http://www.tidemark-harrowgates.example
We were thinking of having the following in a menu bar with drop downs for most...some more than others. Home / For Sale / For Rent / Property 101 / About us / Contact Us ..
Look forward to seeing your ideas. Thanks in advance.

```html
<!DOCTYPE html>
<html lang="en">
<head>
<meta charset="utf-8">
<title>Harbourline Homes</title>
<link rel="stylesheet" href="https://fonts.googleapis.com/css2?family=Roboto:wght@300;400;500;700&display=swap">
<style>
:root{
  --purple:#9b33c9;
  --dark:#3a3d40;
  --text:#333;
  --muted:#8a8a8a;
  --line:#dedede;
  --page:#f4f4f4;
  --white:#fff;
}
*{box-sizing:border-box;margin:0;padding:0}
html,body{width:921px;height:1200px;overflow:hidden}
body{position:relative;background:var(--page);font-family:'Roboto',sans-serif;color:var(--text)}
.abs{position:absolute}
/* header */
.site-header{left:0;top:0;width:921px;height:84px;background:var(--white)}
.topbar{left:156px;top:0;width:610px;height:24px;border-bottom:1px solid var(--line)}
.topbar-mail{left:0;top:7px;font-size:7px;color:var(--muted);display:flex;align-items:center;gap:4px}
.social{right:0;top:0;display:flex;height:24px}
.social span{width:26px;height:24px;border-left:1px solid var(--line);display:flex;align-items:center;justify-content:center}
.social span i{width:7px;height:7px;background:#999;border-radius:50%}
.brand{left:158px;top:38px;display:flex;align-items:center;gap:5px}
.brand-mark{width:14px;height:14px;background:var(--purple)}
.brand-name{font-size:10px;font-weight:500;color:var(--dark);letter-spacing:.5px}
.nav{left:271px;top:59px;display:flex;height:25px}
.nav a{font-size:8.5px;color:#555;text-decoration:none;padding:0 9px;line-height:25px}
.nav a.active{background:var(--purple);color:var(--white);padding:0 9px}
.enquire{right:162px;top:52px;text-align:right}
.enquire small{display:block;font-size:6.5px;color:var(--muted)}
.enquire strong{font-size:13px;color:var(--purple);font-weight:500;display:flex;align-items:center;gap:4px;justify-content:flex-end;margin-top:2px}
/* hero */
.hero{left:0;top:84px;width:921px;height:329px;background:linear-gradient(100deg,#8d8f92 0%,#d9d9d9 30%,#ececec 55%,#a9aaac 80%,#cfd0d1 100%)}
.hero-caption{left:156px;top:178px;width:254px;height:76px;background:rgba(255,255,255,.72);padding:11px 12px}
.hero-caption h2{font-size:12.5px;font-weight:500;color:#222}
.hero-caption p{font-size:6.5px;line-height:12px;color:#555;margin-top:5px}
.hero-caption .price{font-size:9.5px;color:#333;margin-top:3px}
.btn-more{left:156px;top:254px;width:49px;height:18px;background:var(--purple);color:#fff;font-size:6.5px;line-height:18px;text-align:center}
.hero-arrow{top:214px;width:24px;height:24px;border:2px solid #444;border-radius:50%}
.find-tab{left:156px;top:386px;width:144px;height:27px;background:var(--dark);color:#fff;display:flex;align-items:center}
.find-tab .ico{width:28px;height:27px;background:#2c2f31;display:flex;align-items:center;justify-content:center}
.find-tab b{font-size:11px;font-weight:500;margin-left:10px}
/* search */
.search{left:156px;top:413px;width:610px;height:109px;background:var(--white);border:1px solid var(--line);border-top:0}
.field label{display:block;font-size:7px;color:#444;margin-bottom:4px}
.select{height:18px;border:1px solid #d6d6d6;font-size:7px;color:#777;line-height:16px;padding-left:6px;position:relative}
.select::after{content:"";position:absolute;right:0;top:0;width:14px;height:16px;border-left:1px solid #d6d6d6}
.btn-search{left:542px;top:73px;width:49px;height:18px;background:var(--purple);color:#fff;font-size:6.5px;line-height:18px;text-align:center}
/* featured */
.featured{left:156px;top:522px;width:610px;height:280px;border-left:1px solid var(--line);border-right:1px solid var(--line)}
.featured h3{position:absolute;left:27px;top:26px;font-size:13px;font-weight:500;color:#222}
.featured .lead{position:absolute;left:27px;top:47px;font-size:6.8px;color:var(--muted)}
.card{top:80px;width:127px}
.card .photo{width:127px;height:84px}
.card h4{font-size:7px;font-weight:400;color:#333;margin-top:10px}
.card p{font-size:6.3px;line-height:11px;color:var(--muted);margin-top:4px}
.card .tag{display:inline-block;background:var(--dark);color:#fff;font-size:6.3px;padding:2px 5px;margin-top:6px}
.side-arrow{width:14px;height:20px;display:flex;align-items:center;justify-content:center}
/* partners */
.partners{left:156px;top:802px;width:610px;height:84px;background:var(--white);border:1px solid var(--line);border-top:1px solid var(--line)}
.partners-tab{left:260px;top:-1px;width:86px;height:20px;background:var(--dark);color:#fff;font-size:6.8px;line-height:20px;text-align:center}
.badge{top:37px;width:72px;height:20px;background:#e2e2e2;border-radius:3px}
/* footer */
.footer-col{top:909px;width:150px}
.footer-col h5{font-size:9.5px;font-weight:400;color:#333;margin-bottom:14px}
.footer-col p,.footer-col li{font-size:6.3px;line-height:11px;color:#777}
.footer-col p+p{margin-top:11px}
.footer-col ul{list-style:none}
.footer-col li{margin-bottom:5px;padding-left:6px;position:relative}
.footer-col li::before{content:"";position:absolute;left:0;top:4px;border-left:3px solid #555;border-top:2px solid transparent;border-bottom:2px solid transparent}
.footer-rule{left:156px;top:1038px;width:610px;border-top:1px solid #e0e0e0}
.copy{left:156px;top:1053px;font-size:6.5px;color:#777}
.legal{right:158px;top:1053px;font-size:6.5px;color:#777}
.skyline{left:0;top:1072px;width:921px;height:128px;background:linear-gradient(180deg,rgba(200,200,200,0) 0%,#d6d6d6 35%,#bdbdbd 100%)}
</style>
</head>
<body>

<header class="abs site-header">
  <div class="abs topbar">
    <div class="abs topbar-mail">
      <svg width="8" height="7" viewBox="0 0 8 7"><rect x=".5" y="1.5" width="7" height="5" fill="none" stroke="#999"/><path d="M.5 1.5 4 4.5 7.5 1.5" fill="none" stroke="#999"/></svg>
      Email us at : info@harbourlinehomes.example
    </div>
    <div class="abs social"><span><i></i></span><span><i></i></span><span><i></i></span><span><i></i></span><span><i></i></span><span style="border-right:1px solid var(--line)"><i></i></span></div>
  </div>
  <div class="abs brand"><span class="brand-mark"></span><span class="brand-name">HARBOURLINE</span></div>
  <nav class="abs nav">
    <a class="active" href="#">Home</a><a href="#">For Sale</a><a href="#">For Rent</a><a href="#">Property 101</a><a href="#">About us</a><a href="#">Contact Us</a>
  </nav>
  <div class="abs enquire">
    <small>For inquiries, please call us:</small>
    <strong><svg width="10" height="10" viewBox="0 0 10 10"><path d="M2 1 4 3 3 4.5Q4.5 6.5 5.5 7L7 6 9 8 7.5 9.5Q3 8.5.5 2.5Z" fill="none" stroke="#888" stroke-width=".9"/></svg>1-800-555-0192</strong>
  </div>
</header>

<section class="abs hero" role="img" aria-label="Photo of a bright modern living room with leather lounge chairs, a glass coffee table and large windows"></section>
<div class="abs hero-caption">
  <h2>7400 Linden Cres, Harbour Point 3315</h2>
  <p>Lorem ipsum dolor sit amet, consectetu adipiscing elit, sed diam nonummy<br>nibh euismod tincidunt ut laoreet dolore</p>
  <div class="price">$380,000</div>
</div>
<div class="abs btn-more">Know More</div>
<div class="abs hero-arrow" style="left:28px"><svg width="20" height="20" viewBox="0 0 20 20"><path d="M12 5 7 10l5 5" fill="none" stroke="#444" stroke-width="2"/></svg></div>
<div class="abs hero-arrow" style="left:840px;border-color:#fff"><svg width="20" height="20" viewBox="0 0 20 20"><path d="M8 5l5 5-5 5" fill="none" stroke="#fff" stroke-width="2"/></svg></div>
<div class="abs find-tab"><span class="ico"><svg width="10" height="10" viewBox="0 0 10 10"><circle cx="4" cy="4" r="3" fill="none" stroke="#fff" stroke-width="1.4"/><path d="M6.2 6.2 9 9" stroke="#fff" stroke-width="1.6"/></svg></span><b>Find your Home</b></div>

<form class="abs search">
  <div class="abs field" style="left:16px;top:19px;width:186px"><label>Location</label><div class="select">Select</div></div>
  <div class="abs field" style="left:215px;top:19px;width:182px"><label>Status</label><div class="select">Select</div></div>
  <div class="abs field" style="left:410px;top:19px;width:181px"><label>Bedrooms</label><div class="select">Select</div></div>
  <div class="abs field" style="left:16px;top:64px;width:118px"><label>Bathrooms</label><div class="select">Select</div></div>
  <div class="abs field" style="left:146px;top:64px;width:120px"><label>Minimum Price</label><div class="select">Select</div></div>
  <div class="abs field" style="left:277px;top:64px;width:120px"><label>Maximum Price</label><div class="select">Select</div></div>
  <div class="abs field" style="left:410px;top:64px;width:118px"><label>Property Type</label><div class="select">Select</div></div>
  <div class="abs btn-search">Search</div>
</form>

<section class="abs featured">
  <h3>Featured Properties</h3>
  <p class="lead">Look at our Latest listed properties and check out the facilities on them, We have already sold more than 50,000 Homes.</p>
  <div class="abs side-arrow" style="left:-1px;top:109px;background:#e4e4e4"><svg width="4" height="6"><path d="M4 0 0 3 4 6Z" fill="#555"/></svg></div>
  <div class="abs side-arrow" style="left:594px;top:109px;background:var(--dark)"><svg width="4" height="6"><path d="M0 0 4 3 0 6Z" fill="#fff"/></svg></div>
  <article class="abs card" style="left:27px"><div class="photo" role="img" aria-label="Photo of a living room with white and orange chairs" style="background:linear-gradient(135deg,#6f7d7e,#c9d3d3 60%,#d99a3d)"></div><h4>1200 Amberly Ave Coralvale, HP</h4><p>Lorem ipsum dolor sit amet, consectetu<br>adipiscing elit, sed diam...</p><span class="tag">$740000</span></article>
  <article class="abs card" style="left:170px"><div class="photo" role="img" aria-label="Photo of a modern house exterior with a lawn" style="background:linear-gradient(180deg,#b7c7d4,#8e9aa0 55%,#6d8f3e)"></div><h4>7400 Linden Cres, Harbour Point 3315</h4><p>Lorem ipsum dolor sit amet, consectetu<br>adipiscing elit, sed diam...</p><span class="tag">$820000</span></article>
  <article class="abs card" style="left:312px"><div class="photo" role="img" aria-label="Photo of a white lounge with sofa and shelves" style="background:linear-gradient(180deg,#8a8476,#d8d6d0 60%,#b8bcbc)"></div><h4>60 Marlow Way Harbour Point 3313</h4><p>Lorem ipsum dolor sit amet, consectetu<br>adipiscing elit, sed diam...</p><span class="tag">$570000</span></article>
  <article class="abs card" style="left:454px"><div class="photo" role="img" aria-label="Photo of a room with a yellow chair and a television shelf" style="background:linear-gradient(180deg,#d7d4cf,#e9e6e0 55%,#d8b028)"></div><h4>3015 Grove Ave, Palm Crescent</h4><p>Lorem ipsum dolor sit amet, consectetu<br>adipiscing elit, sed diam...</p><span class="tag">$930000</span></article>
</section>

<section class="abs partners">
  <div class="abs partners-tab">Featured Partners</div>
  <div class="abs side-arrow" style="left:-1px;top:36px;background:#e4e4e4"><svg width="4" height="6"><path d="M4 0 0 3 4 6Z" fill="#555"/></svg></div>
  <div class="abs side-arrow" style="left:595px;top:36px;background:#e4e4e4"><svg width="4" height="6"><path d="M0 0 4 3 0 6Z" fill="#555"/></svg></div>
  <div class="abs badge" style="left:35px"></div>
  <div class="abs badge" style="left:132px"></div>
  <div class="abs badge" style="left:208px"></div>
  <div class="abs badge" style="left:305px"></div>
  <div class="abs badge" style="left:396px"></div>
  <div class="abs badge" style="left:494px"></div>
</section>

<footer>
  <div class="abs footer-col" style="left:156px">
    <h5>About Harbourline Homes</h5>
    <p>Aquam est tortor, sagittis in fringilla in, pellent esque nec erat. Aenean semper, neque non faucibus.</p>
    <p>Malesuada, dui felis tempor felis, vel varius ante diam ut mauris.</p>
  </div>
  <div class="abs footer-col" style="left:312px;display:flex;gap:18px;flex-wrap:wrap">
    <h5 style="width:100%">Quick Links</h5>
    <ul><li>Single Family</li><li>New Construction</li><li>On Rent</li><li>On Sale</li></ul>
    <ul><li>Single Family</li><li>New Construction</li><li>On Rent</li><li>On Sale</li></ul>
  </div>
  <div class="abs footer-col" style="left:468px">
    <h5>Quick Links</h5>
    <ul><li>Aquam est tortor, sagittis in fringilla in, pell esque nec erat.</li><li style="margin-top:6px">Aenean semper, neque non faucibus.</li><li style="margin-top:6px">Malesuada, dui felis tempor felis, vel varius</li></ul>
  </div>
  <div class="abs footer-col" style="left:625px">
    <h5>Contact Info</h5>
    <p>3015 Grove Ave, Palm Crescent.<br>Marlow Way, HP 12345-1234.</p>
    <p>Phone : 123-456-0190</p>
    <p>Email : info@harbourlinehomes.example</p>
  </div>
  <div class="abs footer-rule"></div>
  <div class="abs copy">© 2014 All Rights Reserved by Harbourline Homes</div>
  <div class="abs legal">Site Map &nbsp;&nbsp; / &nbsp;&nbsp; Privacy Policy</div>
  <div class="abs skyline" role="img" aria-label="Grey city skyline silhouette along the bottom of the page"></div>
</footer>

</body>
</html>
```